Stationery and Biz Cards for a Publishing Solutions Company
Bram Keswick Publishing Solutions, LLC
Simple
Lyle R. Pennock
President/Managing Editor
478 Birchfield Hollow Road
Larkmoor, OH 44907
lyle.pennock@bramkeswickbooks.example
www.bramkeswickbooks.example
Here is the company logo.

```html
<!DOCTYPE html>
<html lang="en">
<head>
<meta charset="utf-8">
<title>Bram Keswick Publishing Solutions – Business Card</title>
<link href="https://fonts.googleapis.com/css2?family=Montserrat:wght@300;400;600;700&display=swap" rel="stylesheet">
<style>
  :root{
    --stage:#e9eaec;
    --card-white:#ffffff;
    --brand-blue:#1f2a8c;
    --brand-blue-deep:#141c63;
    --brand-blue-bright:#2f47c9;
    --silver:#b9bcc4;
    --ink-grey:#6b6e76;
    --back-dark:#3c3e43;
    --back-light:#6a6c71;
    --back-text:#e6e7ea;
  }
  html,body{margin:0;padding:0;width:1200px;height:901px;overflow:hidden;background:var(--stage);font-family:"Montserrat",Arial,sans-serif;}
  .canvas{position:relative;width:1200px;height:901px;}
  .card{position:absolute;left:280px;width:640px;height:366px;border-radius:4px;overflow:hidden;box-shadow:0 10px 30px rgba(0,0,0,.18);}
  .card-front{top:70px;background:var(--card-white);}
  .card-back{top:466px;background:linear-gradient(135deg,var(--back-light),var(--back-dark));}
  .wave{position:absolute;inset:0;width:100%;height:100%;}

  .brand{position:absolute;top:40px;right:44px;display:flex;align-items:center;gap:12px;}
  .brand-square{width:34px;height:34px;background:var(--brand-blue);flex:none;}
  .brand-name{font-weight:600;font-size:15px;line-height:1.25;color:var(--brand-blue);letter-spacing:.04em;text-transform:uppercase;}

  .person{position:absolute;left:44px;top:150px;}
  .person-name{margin:0;font-weight:700;font-size:22px;line-height:1.2;color:var(--brand-blue);}
  .person-title{margin:4px 0 0;font-weight:400;font-size:12px;color:var(--ink-grey);}

  .contact{position:absolute;left:44px;bottom:30px;margin:0;padding:0;list-style:none;color:#fff;font-size:11.5px;line-height:1.7;}
  .contact li{display:flex;align-items:center;gap:7px;}
  .contact svg{width:11px;height:11px;fill:#fff;flex:none;}
  .contact .no-icon{padding-left:18px;}

  .back-name{position:absolute;left:0;right:0;top:140px;text-align:center;font-weight:300;font-size:30px;color:var(--back-text);letter-spacing:.06em;margin:0;}
  .back-url{position:absolute;left:0;right:0;top:226px;text-align:center;font-weight:400;font-size:11px;color:var(--back-text);letter-spacing:.18em;margin:0;}
</style>
</head>
<body>
<main class="canvas">
  <section class="card card-front" aria-label="Business card front">
    <svg class="wave" viewBox="0 0 640 366" preserveAspectRatio="none" aria-hidden="true">
      <defs>
        <linearGradient id="waveBlue" x1="0" y1="0" x2="1" y2="1">
          <stop offset="0" stop-color="#2f47c9"/>
          <stop offset="1" stop-color="#141c63"/>
        </linearGradient>
      </defs>
      <path d="M0,196 C210,262 430,246 640,110 L640,128 C430,262 210,278 0,214 Z" fill="#b9bcc4"/>
      <path d="M0,224 C210,288 440,268 640,140 L640,366 L0,366 Z" fill="url(#waveBlue)"/>
    </svg>

    <div class="brand">
      <span class="brand-square"></span>
      <span class="brand-name">Bram Keswick<br>Publishing Solutions, LLC</span>
    </div>

    <div class="person">
      <h1 class="person-name">Lyle R. Pennock</h1>
      <p class="person-title">President/Managing Editor</p>
    </div>

    <ul class="contact">
      <li class="no-icon">478 Birchfield Hollow Road</li>
      <li class="no-icon">Larkmoor, OH 44907</li>
      <li><svg viewBox="0 0 24 24"><path d="M6.6 10.8a15 15 0 0 0 6.6 6.6l2.2-2.2a1 1 0 0 1 1-.25 11.4 11.4 0 0 0 3.6.57 1 1 0 0 1 1 1V20a1 1 0 0 1-1 1A17 17 0 0 1 3 4a1 1 0 0 1 1-1h3.5a1 1 0 0 1 1 1c0 1.25.2 2.45.57 3.6a1 1 0 0 1-.25 1z"/></svg>555 010 0182</li>
      <li><svg viewBox="0 0 24 24"><path d="M2 5h20v14H2z M4 7v.5l8 5 8-5V7z" fill-rule="evenodd"/></svg>lyle.pennock@bramkeswickbooks.example</li>
    </ul>
  </section>

  <section class="card card-back" aria-label="Business card back">
    <p class="back-name">Bram Keswick</p>
    <p class="back-url">www.bramkeswickbooks.example</p>
  </section>
</main>
</body>
</html>
```